Fun Trendy High End Spa Services
Business Card, Gift Certificate, Gift Certificate Envelope
I need double sided standard sized Business Card [3.5" x 2"]
We like what is in logo that was uploaded but please use your creativity. We are open to any ideas.
Simple
Lena Harbus LMT
Owner
Mobile
BP@BrightPebblo.com
BrightPebblo.com
We are open to all concepts. So please be creative. This is for Very high end spa service so it needs to look very good. We thought black paper for a base on business cards, gift certificate and GC envelope but are open to any and all ideas! Thank You! We will pick a winner early if we find the perfect design.
"The greatest wealth is health"
(Doesnt need " " on there just use your own idea and play with it.)
Here is The winning logo design. We really like the style but please feel free to be creative with it! Thank you so much!
This is the style of gift certificate that we want designed to match our business card.

```html
<!DOCTYPE html>
<html lang="en">
<head>
<meta charset="utf-8">
<title>Bright Pebblo – Business Card</title>
<link rel="stylesheet" href="https://fonts.googleapis.com/css2?family=Arimo:ital,wght@0,400;0,700;1,400&family=Comfortaa:wght@400&display=swap">
<style>
  :root {
    --backdrop: #3b2e30;
    --card-center: #5a5a5c;
    --card-mid: #2a2a2b;
    --card-edge: #0b0b0b;
    --silver: #d6d6d6;
    --rule: #9a9a9a;
    --accent: #e6157a;
    --white: #ffffff;
  }
  html, body {
    margin: 0;
    padding: 0;
    width: 1200px;
    height: 901px;
    overflow: hidden;
    background: var(--backdrop);
  }
  .stage {
    position: relative;
    width: 1200px;
    height: 901px;
  }
  .card {
    position: absolute;
    left: 312px;
    width: 576px;
    height: 324px;
    border-radius: 28px;
    background: radial-gradient(ellipse 60% 65% at 50% 42%, var(--card-center) 0%, var(--card-mid) 55%, var(--card-edge) 100%);
    box-shadow: 0 6px 18px rgba(0,0,0,0.55);
    overflow: hidden;
    font-family: "Arimo", Arial, sans-serif;
    color: var(--white);
  }
  .card--front { top: 110px; }
  .card--back  { top: 462px; }

  /* front */
  .front-rule {
    position: absolute;
    top: 148px;
    height: 2px;
    background: var(--rule);
  }
  .front-rule--left  { left: 0; width: 190px; }
  .front-rule--right { right: 0; width: 190px; }
  .front-brand {
    position: absolute;
    top: 128px;
    left: 0;
    width: 576px;
    text-align: center;
    font-family: "Comfortaa", sans-serif;
    font-size: 28px;
    line-height: 40px;
    color: var(--silver);
  }
  .front-motto {
    position: absolute;
    top: 262px;
    left: 0;
    width: 576px;
    text-align: center;
    font-size: 16px;
    font-weight: 700;
    color: var(--silver);
  }
  .front-web {
    position: absolute;
    top: 302px;
    left: 0;
    width: 576px;
    text-align: center;
    font-size: 11px;
    color: var(--accent);
  }

  /* back */
  .owner {
    position: absolute;
    top: 30px;
    left: 406px;
    width: 170px;
  }
  .owner-name {
    font-size: 21px;
    font-weight: 700;
    color: var(--accent);
    line-height: 26px;
  }
  .owner-role {
    font-size: 18px;
    font-style: italic;
    line-height: 26px;
    padding-bottom: 4px;
    border-bottom: 2px solid var(--white);
  }
  .back-brand {
    position: absolute;
    top: 112px;
    left: 0;
    width: 576px;
    text-align: center;
    font-family: "Comfortaa", sans-serif;
    font-size: 44px;
    line-height: 50px;
    color: var(--silver);
    letter-spacing: 1px;
  }
  .back-brand-dot {
    display: inline-block;
    width: 30px;
    height: 30px;
    border-radius: 50%;
    border: 3px solid var(--silver);
    margin-right: 14px;
    vertical-align: -2px;
  }
  .back-tagline {
    position: absolute;
    top: 196px;
    left: 0;
    width: 576px;
    text-align: center;
    font-size: 19px;
    color: var(--white);
  }
  .contact {
    position: absolute;
    left: 24px;
    top: 274px;
    font-size: 13px;
    line-height: 18px;
    border-collapse: collapse;
  }
  .contact td { padding: 0; }
  .contact .label { width: 74px; }
</style>
</head>
<body>
<main class="stage">
  <section class="card card--front" aria-label="Card front">
    <div class="front-rule front-rule--left"></div>
    <div class="front-rule front-rule--right"></div>
    <div class="front-brand">Bright Pebblo</div>
    <p class="front-motto" style="margin:0">**The Greatest Wealth Is Health**</p>
    <div class="front-web">www.brightpebblo.com</div>
  </section>

  <section class="card card--back" aria-label="Card back">
    <div class="owner">
      <div class="owner-name">Lena Harbus LMT</div>
      <div class="owner-role">Owner</div>
    </div>
    <div class="back-brand"><span class="back-brand-dot"></span>Bright Pebblo</div>
    <div class="back-tagline">Luxury In Home Spa Experience</div>
    <table class="contact">
      <tr><td class="label">Phone</td><td>: (555) 014-2287</td></tr>
      <tr><td class="label">Website</td><td>: www.brightpebblo.com</td></tr>
    </table>
  </section>
</main>
</body>
</html>
```